Lena Corvell Business Card

I need a business card that reflects my current website: itslenacorvell.example and screenshot attached. If we keep the color scheme of the site and sample card below that would be ideal. The business card should include the information on the attached sample cards.

Industry/Entity Type

Business

```html
<!DOCTYPE html>
<html lang="en">
<head>
<meta charset="utf-8">
<title>Lena Corvell Business Card</title>
<link rel="stylesheet" href="https://fonts.googleapis.com/css2?family=Source+Sans+3:wght@400;600;700&display=swap">
<style>
  :root {
    --page-bg: #efece6;
    --teal: #5ec0ad;
    --white: #ffffff;
    --ink: #1c1c1c;
    --handle-grey: #7a6f74;
    --dot-grey: #c9c9c9;
    --icon-grey: #6b6b6b;
    --signature-tone: #e6e6e6;
  }
  * { margin: 0; padding: 0; box-sizing: border-box; }
  html, body {
    width: 1200px;
    height: 926px;
    overflow: hidden;
    background: var(--page-bg);
    font-family: "Source Sans 3", sans-serif;
  }
  .card {
    position: absolute;
    left: 50px;
    top: 94px;
    width: 1100px;
    height: 738px;
    background: var(--teal);
    box-shadow: 0 6px 18px rgba(0, 0, 0, 0.18);
    overflow: hidden;
  }
  .social {
    position: absolute;
    right: 40px;
    top: 67px;
    height: 36px;
    display: flex;
    align-items: center;
    gap: 10px;
  }
  .social-dot {
    width: 34px;
    height: 34px;
    border-radius: 50%;
    background: var(--icon-grey);
  }
  .social-handle {
    font-size: 23px;
    color: var(--handle-grey);
    font-weight: 400;
  }
  .roles {
    position: absolute;
    left: 0;
    right: 0;
    top: 186px;
    text-align: center;
    font-size: 40px;
    font-weight: 400;
    color: var(--ink);
    letter-spacing: 0.2px;
  }
  .contact {
    position: absolute;
    left: 46px;
    top: 340px;
    color: var(--white);
    font-size: 30px;
    line-height: 43px;
    font-weight: 400;
  }
  .signature-band {
    position: absolute;
    left: 0;
    top: 451px;
    width: 100%;
    height: 176px;
    background: var(--white);
  }
  .band-dots {
    position: absolute;
    left: 0;
    width: 100%;
    height: 3px;
  }
  .band-dots.top { top: 4px; }
  .band-dots.bottom { bottom: 4px; }
  .signature-mark {
    position: absolute;
    left: 615px;
    top: 22px;
    width: 400px;
    height: 130px;
    background: linear-gradient(90deg, var(--white), var(--signature-tone) 40%, var(--white));
  }
  .website {
    position: absolute;
    left: 0;
    right: 0;
    top: 664px;
    text-align: center;
    color: var(--white);
    font-size: 36px;
    font-weight: 700;
    letter-spacing: 0.3px;
  }
</style>
</head>
<body>
  <main class="card">
    <div class="social">
      <span class="social-dot"></span>
      <span class="social-handle">@itslenacorvell</span>
    </div>

    <p class="roles">Brand Curator&#8202;|&#8202;Digital Storyteller | Social Entrpreneur</p>

    <div class="contact">
      <p class="contact-email">me@lenacorvell.example</p>
      <p class="contact-phone">555.014.2297</p>
    </div>

    <section class="signature-band">
      <svg class="band-dots top" viewBox="0 0 1100 3" preserveAspectRatio="none">
        <line x1="0" y1="1.5" x2="1100" y2="1.5" stroke="var(--dot-grey)" stroke-width="2" stroke-dasharray="2 6"/>
      </svg>
      <div class="signature-mark" role="img" aria-label="Hand-lettered signature reading 'iam Lena Corvell' in black ink"></div>
      <svg class="band-dots bottom" viewBox="0 0 1100 3" preserveAspectRatio="none">
        <line x1="0" y1="1.5" x2="1100" y2="1.5" stroke="var(--dot-grey)" stroke-width="2" stroke-dasharray="2 6"/>
      </svg>
    </section>

    <p class="website">www.itslenacorvell.example</p>
  </main>
</body>
</html>
```